Stationery Design Project

Brivan-Holt Consultants is interim management company. We are specialized in finding the best Finance and IT consultants for our clients when they require additional resources on an interim basis for projects or special situations. We are flexible in our approach and we always seek to maximize the benefits for our clients as well as our consultants.

We are looking for a design of our letterhead, general stationery and business cards using the company name. The design will also be found on our coming web pages.
Updates

Please also create a logo for Brivan-Holt Consultants which expresses that we want to match the best finance and IT people to our customers projects

Target Market(s)

Larger and mid sized companies (all sectors), as well as highly skilled Finance & IT professionals/consultants

Industry/Entity Type

Business

Requirements
Must have
• Brivan-Holt Consultants
We are expecting that 'Brivan-Holt' will be on the first line and 'Consultants' on a second line.
Please also indicate style of the letters for our address/phone and mail details. Our current address is:
Tarnvoldgade 9,
2870 Kalsbro
Danmark
Mobile: +45 XX XX XX XX Mail: xx@brivan-holt.dk

```html
<!DOCTYPE html>
<html lang="en">
<head>
<meta charset="utf-8">
<title>Brivan-Holt Consultants – Business Card</title>
<link href="https://fonts.googleapis.com/css2?family=Arimo:wght@400;700&display=swap" rel="stylesheet">
<style>
  :root {
    --stage: #e4e4e4;
    --card: #ffffff;
    --ink: #4a4a4a;
    --ink-soft: #6a6a6a;
    --brand: #1f6fc2;
    --brand-deep: #1d4fa0;
    --brand-light: #2d8fe0;
    --rule-dark: #3a3a3a;
    --on-brand: #ffffff;
  }
  * { margin: 0; padding: 0; box-sizing: border-box; }
  html, body {
    width: 1200px; height: 819px; overflow: hidden;
    background: var(--stage);
    font-family: "Arimo", Arial, sans-serif;
  }
  .stage { position: relative; width: 1200px; height: 819px; }

  .card {
    position: absolute;
    background: var(--card);
    border-radius: 18px;
    overflow: hidden;
    box-shadow: 0 6px 18px rgba(0,0,0,0.25);
  }

  /* Front */
  .card-front { left: 50px; top: 232px; width: 640px; height: 354px;
    background: linear-gradient(180deg, #ffffff 0%, #f3f3f3 58%); }
  .holder { position: absolute; right: 40px; top: 48px; text-align: right; }
  .holder-name { font-size: 22px; font-weight: 700; color: var(--ink); }
  .holder-role { font-size: 14px; color: var(--ink-soft); margin-top: 8px; }

  .rule-dark { position: absolute; left: 0; top: 206px; width: 250px; height: 5px; background: var(--rule-dark); }
  .rule-brand { position: absolute; left: 0; top: 203px; width: 100%; height: 4px; background: var(--brand); }
  .band { position: absolute; left: 0; top: 211px; width: 100%; height: 143px;
    background: radial-gradient(ellipse at 35% 20%, var(--brand-light) 0%, var(--brand) 45%, var(--brand-deep) 100%); }

  .front-mark { position: absolute; left: 38px; top: 146px; display: flex; align-items: center; gap: 12px; }
  .mark-dot { width: 66px; height: 66px; border-radius: 50%; background: var(--brand); border: 3px solid #fff;
    box-shadow: 0 1px 4px rgba(0,0,0,0.3); }
  .wordmark { color: var(--brand); font-weight: 400; line-height: 1; }
  .wordmark-name { font-size: 36px; letter-spacing: -0.5px; }
  .wordmark-sub { font-size: 13px; letter-spacing: 3px; margin-top: 2px; }

  .address { position: absolute; left: 80px; top: 236px; color: var(--on-brand); font-size: 13px; line-height: 17px; }
  .contacts { position: absolute; left: 308px; top: 236px; list-style: none; color: var(--on-brand); font-size: 13.5px; letter-spacing: 0.3px; }
  .contacts li { display: flex; align-items: center; height: 17px; gap: 4px; }
  .contacts svg { width: 15px; height: 13px; fill: none; stroke: var(--on-brand); stroke-width: 1.4; }

  /* Back */
  .card-back { left: 790px; top: 90px; width: 354px; height: 640px;
    background: linear-gradient(160deg, #ffffff 0%, #efefef 100%); }
  .back-mark { position: absolute; left: 0; top: 235px; width: 100%; display: flex; flex-direction: column; align-items: center; gap: 16px; }
  .back-mark .mark-dot { width: 96px; height: 96px; }
  .back-mark .wordmark { text-align: center; }
  .back-mark .wordmark-name { font-size: 42px; }
  .back-mark .wordmark-sub { font-size: 15px; letter-spacing: 4px; margin-top: 4px; }
</style>
</head>
<body>
<main class="stage">
  <section class="card card-front" aria-label="Business card front">
    <div class="holder">
      <p class="holder-name">Marten Skov</p>
      <p class="holder-role">CEO</p>
    </div>
    <div class="band"></div>
    <div class="rule-brand"></div>
    <div class="rule-dark"></div>
    <div class="front-mark">
      <span class="mark-dot"></span>
      <div class="wordmark">
        <p class="wordmark-name">Brivan-Holt</p>
        <p class="wordmark-sub">Consultants</p>
      </div>
    </div>
    <address class="address" style="font-style:normal">
      Tarnvoldgade 9, 2870 Kalsbro<br>Danmark
    </address>
    <ul class="contacts">
      <li><svg viewBox="0 0 16 14"><path d="M4 2 C2 4 3 8 7 11 C9 12.5 11 12.5 12 11 L10 9 L8.5 10 C7 9 5.5 7.5 5 6 L6 4.5 Z"/></svg>: 813-555-0148</li>
      <li><svg viewBox="0 0 16 14"><path d="M2 5 Q8 0 14 5 L12 6 L11 4.5 H5 L4 6 Z M4 7 H12 L13 12 H3 Z"/></svg>: 1-877-555-0192</li>
      <li><svg viewBox="0 0 16 14"><rect x="2" y="3" width="12" height="8"/><path d="M2 3 L8 8 L14 3"/></svg>: info@brivanholtgroup.com</li>
      <li><svg viewBox="0 0 16 14"><path d="M6 9 L10 5 M7 4 L9 2 Q11 1 12.5 2.5 Q13.5 4 12 6 L10 8 M9 10 L7 12 Q5 13 3.5 11.5 Q2.5 10 4 8 L6 6"/></svg>: brivanholtgroup.com</li>
    </ul>
  </section>

  <section class="card card-back" aria-label="Business card back">
    <div class="back-mark">
      <span class="mark-dot"></span>
      <div class="wordmark">
        <p class="wordmark-name">Brivan-Holt</p>
        <p class="wordmark-sub">Consultants</p>
      </div>
    </div>
  </section>
</main>
</body>
</html>
```